Edgy rebranded biz cards KRB

We are rebranding our 20 yr old mortgage company with a new logo and would like cards to compliment our new look.

Target Market(s)

potential home buyers or clients for refinance

Industry/Entity Type

Mortgage Brokerage

Contact Information for Business Card

418 W. Lomita Ave #305
Henderson, NV 89152
702.519.4827 o
702-519-4829 f
www.kestrelridgelending,example
nmls 842019
KRB is an equal housing lender

Font styles to use
Sans Serif

Colors
0455a3
3176b5
0393ce
33a6d7

Requirements
Must have
• space for a photo
Nice to have
• One side with the company info and the other with the person's info

```html
<!DOCTYPE html>
<html lang="en">
<head>
<meta charset="utf-8">
<title>Kestrel Ridge Lending – Business Card</title>
<link href="https://fonts.googleapis.com/css2?family=Montserrat:wght@600;700&family=Poppins:wght@400;500&family=Noto+Serif:ital@1&display=swap" rel="stylesheet">
<style>
  :root {
    --brand-blue: #1272bd;
    --brand-grey: #7d7e82;
    --ink: #2b2b2b;
    --paper: #ffffff;
    --backdrop: #e7e4df;
  }
  * { margin: 0; padding: 0; box-sizing: border-box; }
  html, body { width: 900px; height: 1200px; overflow: hidden; }
  body { background: var(--backdrop); position: relative; font-family: "Poppins", sans-serif; }

  .card {
    position: absolute; left: 82px; width: 738px; height: 433px;
    border-radius: 30px; overflow: hidden;
    box-shadow: 0 6px 18px rgba(0,0,0,.25);
  }
  .card--front { top: 137px; background: var(--paper); }
  .card--back { top: 640px; background: var(--brand-blue); }

  .photo-area {
    position: absolute; left: 368px; top: 0; width: 370px; height: 394px;
    clip-path: polygon(0 262px, 204px 0, 370px 0, 370px 394px, 0 394px);
    background: linear-gradient(90deg, #8a8b8f 0%, #a9aaae 30%, #cfd0d3 60%, #9c9da1 100%);
  }

  .footer-bands { position: absolute; left: 0; bottom: 0; }

  .brand { position: absolute; left: 40px; top: 58px; width: 300px; }
  .brand__name {
    font-family: "Montserrat", sans-serif; font-weight: 700;
    color: var(--brand-blue); font-size: 33px; line-height: 1.15; letter-spacing: .3px;
  }
  .brand__tagline {
    position: absolute; left: 40px; top: 175px;
    font-family: "Noto Serif", serif; font-style: italic;
    color: var(--brand-blue); font-size: 18px;
  }

  .contact { position: absolute; left: 40px; top: 233px; list-style: none; }
  .contact li {
    display: flex; align-items: flex-start; gap: 9px;
    font-size: 16.5px; line-height: 25px; color: var(--ink);
  }
  .contact svg { flex: none; margin-top: 3px; }

  .license {
    position: absolute; left: 40px; top: 395px;
    font-family: "Montserrat", sans-serif; font-weight: 600;
    color: #fff; font-size: 15px;
  }
  .agent {
    position: absolute; left: 475px; top: 405px; color: #fff;
    font-family: "Montserrat", sans-serif; font-weight: 700; font-size: 16px;
  }
  .agent__title { font-family: "Poppins", sans-serif; font-weight: 400; font-size: 12px; margin-left: 3px; }
  .agent__title sup { font-size: 7px; }

  .back-brand {
    position: absolute; left: 0; right: 0; top: 165px; text-align: center;
    font-family: "Montserrat", sans-serif; font-weight: 700;
    color: #fff; font-size: 40px; line-height: 1.1;
  }
  .back-url {
    position: absolute; left: 0; right: 0; top: 380px; text-align: center;
    color: #fff; font-size: 16px; font-weight: 500;
  }
</style>
</head>
<body>

<section class="card card--front">
  <div class="photo-area" role="img" aria-label="Portrait photo of the loan officer in a suit, arms crossed, over a grey house graphic"></div>

  <svg class="footer-bands" width="738" height="39" viewBox="0 394 738 39">
    <polygon points="0,394 360,394 345,413 0,413" fill="var(--brand-grey)"/>
    <polygon points="0,413 345,413 360,394 738,394 738,433 0,433" fill="var(--brand-blue)"/>
  </svg>

  <div class="brand"><p class="brand__name">KESTREL RIDGE<br>LENDING</p></div>
  <p class="brand__tagline">KRB is an equal housing lender</p>

  <ul class="contact">
    <li><svg width="18" height="18" viewBox="0 0 18 18"><circle cx="9" cy="9" r="9" fill="var(--brand-blue)"/><path d="M5 7c0-1 1-2 4-2s4 1 4 2v1h-2V7H7v1H5z M6 9h6l1 3H5z" fill="#fff"/></svg>702.519.4827</li>
    <li><svg width="18" height="18" viewBox="0 0 18 18"><circle cx="9" cy="9" r="9" fill="var(--brand-blue)"/><rect x="6" y="4" width="6" height="3" fill="#fff"/><rect x="4" y="7.5" width="10" height="4" rx="1" fill="#fff"/><rect x="6" y="11" width="6" height="3" fill="#fff"/></svg>702-519-4829</li>
    <li><svg width="18" height="18" viewBox="0 0 18 18"><circle cx="9" cy="9" r="9" fill="var(--brand-blue)"/><g fill="none" stroke="#fff" stroke-width="1.1"><circle cx="9" cy="9" r="5"/><ellipse cx="9" cy="9" rx="2.2" ry="5"/><path d="M4 9h10"/></g></svg>www.kestrelridgelending,example</li>
    <li><svg width="18" height="18" viewBox="0 0 18 18"><path d="M9 0a7 7 0 0 1 7 7c0 5-7 11-7 11S2 12 2 7a7 7 0 0 1 7-7z" fill="var(--brand-blue)"/><circle cx="9" cy="7" r="2.6" fill="#fff"/></svg>418 W. Lomita Ave #305<br>Henderson, NV 89152</li>
  </ul>

  <p class="license">Nmls 842019</p>
  <p class="agent">MARCUS DELANEY <span class="agent__title">Realtor<sup>®</sup></span></p>
</section>

<section class="card card--back">
  <p class="back-brand">KESTREL RIDGE<br>LENDING</p>
  <p class="back-url">www.kestrelridgelending.example</p>
</section>

</body>
</html>
```